4 x Designs Required

Hi There,
I require 4 x different designs to be made for 4 new brands of mine however they can be quite interchangeable. HR Plinkr and Marketing Plinkr can be similar just with a difference in colour. The same goes for the Bulletin brands. This means there are ultimately two designs that need perfecting.

There must be a click here CTA on the banner somewhere. :-)

I require the banners in 728x90 format and 960x90 please.

Please use strap lines on the banners such as:
Essential Whitepapers for HR Professionals
Essential Whitepapers for Marketing Professionals
Your No.1 Whitepaper Resource

The brand names:
HR Plinkr
Marketing Plinkr
HR Dispatchly
Marketing Dispatchly

Examples attached.

```html
<!DOCTYPE html>
<html lang="en">
<head>
<meta charset="utf-8">
<title>Plinkr Banners</title>
<link rel="stylesheet" href="https://fonts.googleapis.com/css2?family=Questrial&family=Montserrat:wght@700&display=swap">
<style>
  :root {
    --page-bg: #ffffff;
    --frame: #b9b9b9;
    --hr-ink: #231f20;
    --hr-text: #2b2b2b;
    --hr-btn-top: #6a6a6a;
    --hr-btn-bottom: #3a3a3a;
    --mk-blue: #1191d0;
    --mk-indigo: #2a0f7a;
    --mk-deep: #33006e;
    --mk-violet: #9a14d2;
    --mk-yellow: #f5c300;
    --mk-btn-top: #fff27a;
    --mk-btn-bottom: #f3c200;
    --white: #ffffff;
  }
  html, body {
    margin: 0;
    padding: 0;
    width: 1200px;
    height: 1200px;
    overflow: hidden;
    background: var(--page-bg);
  }
  .canvas {
    position: relative;
    width: 1200px;
    height: 1200px;
    box-sizing: border-box;
    border: 1px solid var(--frame);
    background: var(--page-bg);
  }
  .banner {
    position: absolute;
    box-sizing: border-box;
    overflow: hidden;
  }
  .banner-art {
    position: absolute;
    inset: 0;
  }
  .brand-name {
    position: absolute;
    margin: 0;
    font-family: "Questrial", sans-serif;
    font-weight: 400;
    white-space: nowrap;
    line-height: 1;
  }
  .strapline {
    position: absolute;
    margin: 0;
    font-family: "Questrial", sans-serif;
    white-space: nowrap;
    line-height: 1;
  }
  .cta {
    position: absolute;
    display: flex;
    align-items: center;
    justify-content: center;
    box-sizing: border-box;
    border-radius: 9px;
    font-family: "Montserrat", sans-serif;
    font-weight: 700;
    font-size: 19px;
    letter-spacing: 0.5px;
    text-decoration: none;
  }

  /* HR banner */
  .banner--hr {
    left: 164px;
    top: 471px;
    width: 873px;
    height: 107px;
    border: 1px solid #8c8c8c;
    background: var(--white);
  }
  .banner--hr .banner-art {
    background:
      linear-gradient(90deg, rgba(255,255,255,1) 0%, rgba(255,255,255,0.2) 25%, rgba(255,255,255,0.55) 55%, rgba(255,255,255,0) 100%),
      linear-gradient(120deg, #ececec 0%, #d6d6d6 35%, #f3f3f3 55%, #bdbdbd 80%, #9e9e9e 100%);
  }
  .banner--hr .brand-name {
    left: 28px;
    top: 30px;
    font-size: 48px;
    color: var(--hr-ink);
  }
  .banner--hr .strapline {
    left: 288px;
    top: 43px;
    font-size: 20px;
    color: var(--hr-text);
  }
  .banner--hr .cta {
    left: 733px;
    top: 32px;
    width: 111px;
    height: 44px;
    color: var(--white);
    background: linear-gradient(180deg, var(--hr-btn-top), var(--hr-btn-bottom));
    box-shadow: 0 1px 2px rgba(0,0,0,0.35);
  }

  /* Marketing banner */
  .banner--marketing {
    left: 25px;
    top: 620px;
    width: 1151px;
    height: 108px;
    border: 1px solid #5a1e8c;
  }
  .banner--marketing .banner-art {
    background: linear-gradient(90deg, var(--mk-blue) 0%, var(--mk-indigo) 28%, var(--mk-deep) 50%, #4a0a96 72%, var(--mk-violet) 100%);
  }
  .banner--marketing .brand-name {
    left: 28px;
    top: 32px;
    font-size: 40px;
    color: var(--mk-yellow);
  }
  .banner--marketing .strapline {
    left: 337px;
    top: 46px;
    font-size: 24px;
    color: var(--white);
  }
  .banner--marketing .cta {
    left: 1004px;
    top: 29px;
    width: 110px;
    height: 44px;
    color: #1c1300;
    background: linear-gradient(180deg, var(--mk-btn-top), var(--mk-btn-bottom));
    box-shadow: 0 1px 3px rgba(0,0,0,0.35);
  }
</style>
</head>
<body>
  <main class="canvas">
    <section class="banner banner--hr">
      <div class="banner-art" role="img" aria-label="Soft grey diagonal plaid pattern background"></div>
      <h2 class="brand-name">HR Plinkr</h2>
      <p class="strapline">Essential Whitepapers for HR Professionals</p>
      <a class="cta" href="#">SIGN UP</a>
    </section>

    <section class="banner banner--marketing">
      <div class="banner-art" role="img" aria-label="Blue to purple gradient background with flowing lines and dot accents"></div>
      <h2 class="brand-name">Marketing Plinkr</h2>
      <p class="strapline">Essential Whitepapers for Marketing Professionals</p>
      <a class="cta" href="#">SIGN UP</a>
    </section>
  </main>
</body>
</html>
```